RV park billboard

We need a billboard for cedar bend RV park . I was thinking about having a big orange in the background. We will have free fiber optic internet and each camper will have its own personal hotspot and we want that on the sign... Also the phone number with the area code... But I don't have the exact number yet. Size of sign will be 12 x 40
Updates
Make sure sign has Cedar Bend RV park on it
Target Market(s)
Plant turnaround workers
Look and feel

```html
<!DOCTYPE html>
<html lang="en">
<head>
<meta charset="utf-8">
<title>Cedar Bend RV Park Billboard</title>
<link href="https://fonts.googleapis.com/css2?family=Montserrat:ital,wght@0,800;1,900&display=swap" rel="stylesheet">
<style>
  :root {
    --backdrop: #646263;
    --paper: #ffffff;
    --ink: #000000;
    --orange: #ee7a12;
    --orange-light: #f19234;
    --orange-deep: #e46c0a;
    --fruit: #e9913f;
  }
  html, body {
    margin: 0;
    padding: 0;
    width: 1200px;
    height: 1200px;
    overflow: hidden;
    background: var(--backdrop);
  }
  .billboard {
    position: absolute;
    left: 29px;
    top: 428px;
    width: 1142px;
    height: 342px;
    font-family: "Montserrat", sans-serif;
  }
  .billboard-shapes {
    position: absolute;
    inset: 0;
  }
  .park-name {
    position: absolute;
    left: 34px;
    margin: 0;
    color: var(--ink);
    font-weight: 800;
    line-height: 1;
    white-space: nowrap;
  }
  .park-name-top {
    top: 126px;
    font-size: 50px;
    letter-spacing: -1px;
  }
  .park-name-bottom {
    top: 192px;
    left: 28px;
    font-size: 98px;
    letter-spacing: -3px;
  }
  .feature-icon {
    position: absolute;
    width: 88px;
    height: 88px;
  }
  .feature-icon.fiber { left: 610px; top: 28px; }
  .feature-icon.hotspot { left: 584px; top: 137px; }
  .feature-text {
    position: absolute;
    margin: 0;
    color: var(--ink);
    font-weight: 900;
    font-style: italic;
    font-size: 40px;
    line-height: 39px;
    letter-spacing: -1px;
    white-space: nowrap;
  }
  .feature-text.fiber { left: 722px; top: 32px; }
  .feature-text.hotspot { left: 696px; top: 141px; }
  .phone {
    position: absolute;
    left: 614px;
    top: 262px;
    display: flex;
    align-items: center;
    gap: 6px;
  }
  .phone-icon { width: 40px; height: 40px; }
  .phone-number {
    color: var(--paper);
    font-weight: 800;
    font-size: 60px;
    line-height: 1;
    letter-spacing: -1px;
  }
</style>
</head>
<body>
<div class="billboard">
  <svg class="billboard-shapes" viewBox="0 0 1142 342" width="1142" height="342">
    <defs>
      <linearGradient id="scene-tone" x1="0" y1="0" x2="1" y2="1">
        <stop offset="0" stop-color="#e86d08"/>
        <stop offset="0.6" stop-color="#ee8424"/>
        <stop offset="1" stop-color="#f2922f"/>
      </linearGradient>
    </defs>
    <polygon points="0,0 679,0 561,333 0,333" fill="var(--paper)"/>
    <polygon points="0,333 564,333 561,342 0,342" fill="var(--ink)"/>
    <polygon points="679,0 690,0 569,342 558,342" fill="var(--ink)"/>
    <polygon class="rv-scene" role="img" aria-label="Photo of a motorhome parked at a campsite, tinted orange"
             points="690,0 1142,0 1142,342 569,342" fill="url(#scene-tone)"/>
    <circle class="orange-fruit" role="img" aria-label="Illustration of a large orange with a green leaf"
            cx="476" cy="134" r="70" fill="var(--fruit)"/>
  </svg>

  <p class="park-name park-name-top">CEDAR BEND</p>
  <p class="park-name park-name-bottom">RV PARK</p>

  <svg class="feature-icon fiber" viewBox="0 0 88 88" aria-hidden="true">
    <circle cx="44" cy="44" r="42" fill="var(--paper)"/>
    <circle cx="44" cy="44" r="36" fill="var(--orange)"/>
    <circle cx="44" cy="44" r="27" fill="none" stroke="var(--paper)" stroke-width="3"/>
    <g fill="none" stroke="var(--paper)" stroke-width="2" stroke-linecap="round">
      <path d="M28 30 Q46 36 58 38"/>
      <path d="M28 34 Q44 42 56 46"/>
      <path d="M28 38 Q40 48 50 54"/>
      <path d="M28 42 Q36 52 42 58"/>
    </g>
    <g fill="var(--paper)">
      <circle cx="59" cy="38" r="2.5"/><circle cx="57" cy="46" r="2.5"/>
      <circle cx="51" cy="55" r="2.5"/><circle cx="43" cy="59" r="2.5"/>
    </g>
  </svg>
  <p class="feature-text fiber">FREE FIBER<br>OPTIC INTERNET</p>

  <svg class="feature-icon hotspot" viewBox="0 0 88 88" aria-hidden="true">
    <circle cx="44" cy="44" r="42" fill="var(--paper)"/>
    <circle cx="44" cy="44" r="36" fill="var(--orange)"/>
    <g fill="none" stroke="var(--paper)" stroke-width="4" stroke-linecap="round">
      <path d="M56 36 A12 10 0 1 0 40 48 L50 48"/>
      <path d="M32 52 A12 10 0 1 0 48 40 L38 40"/>
    </g>
  </svg>
  <p class="feature-text hotspot">PERSONAL<br>HOTSPOT</p>

  <div class="phone">
    <svg class="phone-icon" viewBox="0 0 40 40" aria-hidden="true">
      <path d="M8 8 L14 6 L18 14 L14 17 Q17 24 23 27 L26 23 L34 27 L32 33 Q28 36 22 33 Q10 27 6 15 Q5 10 8 8 Z" fill="var(--ink)"/>
      <g fill="none" stroke="var(--ink)" stroke-width="2" stroke-linecap="round">
        <path d="M22 12 A7 7 0 0 1 28 18"/>
        <path d="M22 6 A13 13 0 0 1 34 18"/>
      </g>
    </svg>
    <span class="phone-number">5550-123-456</span>
  </div>
</div>
</body>
</html>
```